Marrow Aviation Group - "Coming Soon" Main Company Webpage

Design a main webpage that can be posted while a fully functional website is constructed. The design should be created to convey a sense of luxury and exclusivity. The main page should contain only one photo as the background. The photo I believe to show "luxury" and "Exclusivity" is listed as "Global Luxury Photo". I have included two other photos as well to aid in providing a variety of presentations.
The "Member TFPS" logo should appear somewhere on the main page but be less prevalent than the main company logo. "Coming Soon" should also appear to convey that a website is being constructed.
Tabs for the website:
- Aircraft Management
- Aircraft Sales
- Pilot Services
- Charter
- Flight Training

```html
<!DOCTYPE html>
<html lang="en">
<head>
<meta charset="utf-8">
<title>Marrow Aviation Group – Coming Soon</title>
<link rel="stylesheet" href="https://fonts.googleapis.com/css2?family=Michroma&family=Inter:wght@400&display=swap">
<style>
  :root {
    --cobalt: #0a5cad;
    --ink: #111418;
    --page: #ffffff;
    --panel: rgba(250, 250, 250, 0.86);
    --rule: rgba(0, 0, 0, 0.09);
    --field: #fafafa;
    --placeholder: #9a9ea3;
    --sky-light: #eeeeef;
    --sky-mid: #d3d4d6;
    --sky-dark: #a9abae;
    --fuselage: #e9eaec;
  }
  * { box-sizing: border-box; margin: 0; padding: 0; }
  html, body { width: 1200px; height: 1147px; overflow: hidden; background: var(--page); }
  body { position: relative; font-family: "Michroma", sans-serif; color: var(--ink); }

  .screen { position: absolute; overflow: hidden; }
  .backdrop {
    position: absolute; inset: 0;
    background:
      linear-gradient(115deg, transparent 55%, var(--fuselage) 75%, #f4f4f5 100%),
      radial-gradient(ellipse at 30% 70%, var(--sky-dark), transparent 60%),
      linear-gradient(180deg, var(--sky-light) 0%, var(--sky-mid) 55%, #c2c3c6 85%, var(--fuselage) 100%);
  }

  .brand { position: absolute; color: var(--cobalt); line-height: 1; }
  .brand-name { display: block; letter-spacing: 0.02em; }
  .brand-sub { display: block; letter-spacing: 0.08em; }

  .nav { position: absolute; left: 0; right: 0; list-style: none; }
  .nav li { border-top: 1px solid var(--rule); display: flex; align-items: center; }
  .nav li:last-child { border-bottom: 1px solid var(--rule); }

  .member { position: absolute; display: flex; align-items: flex-end; }
  .member-dot { border-radius: 50%; background: var(--cobalt); flex: none; }
  .member-text { display: flex; flex-direction: column; line-height: 1; }
  .member-label { font-family: "Inter", sans-serif; color: #333; }
  .member-name { color: var(--ink); letter-spacing: 0.06em; }

  .headline { position: absolute; color: var(--cobalt); line-height: 1; letter-spacing: 0.01em; font-weight: 400; }
  .tagline { position: absolute; color: var(--ink); }

  .signup { position: absolute; display: flex; }
  .signup input {
    flex: 1; border: 0; background: var(--field); font-family: "Michroma", sans-serif;
    color: var(--ink); outline: none;
  }
  .signup input::placeholder { color: var(--placeholder); }
  .signup button { border: 0; background: var(--cobalt); display: flex; align-items: center; justify-content: center; }

  /* Desktop */
  .desktop { left: 59px; top: 54px; width: 1082px; height: 609px; }
  .desktop .sidebar { position: absolute; left: 0; top: 0; width: 299px; height: 100%; background: var(--panel); }
  .desktop .brand { left: 61px; top: 76px; }
  .desktop .brand-name { font-size: 27px; }
  .desktop .brand-sub { font-size: 10.5px; margin-top: 6px; }
  .desktop .nav { top: 168px; }
  .desktop .nav li { height: 48px; padding-left: 61px; font-size: 9.5px; }
  .desktop .member { left: 61px; top: 538px; gap: 8px; }
  .desktop .member-dot { width: 34px; height: 26px; border-radius: 50%; }
  .desktop .member-label { font-size: 9px; margin-bottom: 4px; }
  .desktop .member-name { font-size: 21px; }
  .desktop .headline { left: 396px; top: 48px; font-size: 72px; }
  .desktop .headline span { display: block; }
  .desktop .headline span + span { margin-top: 8px; }
  .desktop .tagline { left: 397px; top: 200px; font-size: 11.5px; }
  .desktop .signup { left: 397px; top: 248px; width: 414px; height: 38px; }
  .desktop .signup input { padding-left: 18px; font-size: 11px; }
  .desktop .signup button { width: 60px; }

  /* Phones */
  .phone { top: 722px; width: 203px; height: 361px; }
  .phone-home { left: 59px; }
  .phone-menu { left: 297px; }
  .phone .brand { left: 14px; top: 20px; }
  .phone .brand-name { font-size: 12.5px; }
  .phone .brand-sub { font-size: 5px; margin-top: 3px; }
  .phone-menu .sheet { position: absolute; inset: 0; background: var(--panel); }
  .icon-btn { position: absolute; left: 176px; top: 28px; }
  .phone .headline { left: 14px; top: 85px; font-size: 31px; }
  .phone .headline span { display: block; }
  .phone .headline span + span { margin-top: 2px; }
  .phone .tagline { left: 14px; top: 150px; width: 170px; font-size: 7.5px; line-height: 1.45; }
  .phone .signup { left: 14px; top: 193px; width: 177px; height: 27px; }
  .phone .signup input { padding-left: 11px; font-size: 7px; }
  .phone .signup button { width: 39px; }
  .phone .nav { top: 80px; }
  .phone .nav li { height: 32.5px; padding-left: 14px; font-size: 6.5px; }
  .phone .member { left: 14px; top: 323px; gap: 5px; }
  .phone .member-dot { width: 21px; height: 15px; }
  .phone .member-label { font-size: 5px; margin-bottom: 2px; }
  .phone .member-name { font-size: 13px; }
</style>
</head>
<body>

<section class="screen desktop">
  <div class="backdrop" role="img" aria-label="Photograph of a white private jet's engine, tail wing and fuselage against an overcast grey sky"></div>
  <aside class="sidebar">
    <div class="brand"><span class="brand-name">MARROW</span><span class="brand-sub">AVIATION GROUP</span></div>
    <ul class="nav">
      <li>AIRCRAFT MANAGEMENT</li>
      <li>AIRCRAFT SALES</li>
      <li>PILOT SERVICES</li>
      <li>CHARTER</li>
      <li>FLIGHT TRAINING</li>
    </ul>
    <div class="member">
      <span class="member-dot"></span>
      <span class="member-text"><span class="member-label">member of</span><span class="member-name">TFPS</span></span>
    </div>
  </aside>
  <h1 class="headline"><span>COMING</span><span>SOON</span></h1>
  <p class="tagline">Sign up to be the first one to know when we launch.</p>
  <form class="signup">
    <input type="email" placeholder="Email Address">
    <button type="button" aria-label="Sign up">
      <svg width="24" height="14" viewBox="0 0 24 14" fill="none" stroke="#fff" stroke-width="1.6"><path d="M0 7h22M16 1l6 6-6 6"/></svg>
    </button>
  </form>
</section>

<section class="screen phone phone-home">
  <div class="backdrop" role="img" aria-label="Photograph of a white private jet engine and wing under a grey sky"></div>
  <div class="brand"><span class="brand-name">MARROW</span><span class="brand-sub">AVIATION GROUP</span></div>
  <svg class="icon-btn" width="14" height="12" viewBox="0 0 14 12" fill="none" stroke="#111418" stroke-width="1.6" aria-label="Menu"><path d="M0 1h14M0 6h14M5 11h9"/></svg>
  <h1 class="headline"><span>COMING</span><span>SOON</span></h1>
  <p class="tagline">Sign up to be the first one to know when we launch.</p>
  <form class="signup">
    <input type="email" placeholder="Email Address">
    <button type="button" aria-label="Sign up">
      <svg width="22" height="12" viewBox="0 0 22 12" fill="none" stroke="#fff" stroke-width="1.5"><path d="M0 6h20M15 1l5 5-5 5"/></svg>
    </button>
  </form>
</section>

<section class="screen phone phone-menu">
  <div class="backdrop" role="img" aria-label="Photograph of a white private jet under a grey sky"></div>
  <div class="sheet"></div>
  <div class="brand"><span class="brand-name">MARROW</span><span class="brand-sub">AVIATION GROUP</span></div>
  <svg class="icon-btn" width="13" height="13" viewBox="0 0 13 13" fill="none" stroke="#111418" stroke-width="1.6" aria-label="Close menu"><path d="M1 1l11 11M12 1L1 12"/></svg>
  <ul class="nav">
    <li>AIRCRAFT MANAGEMENT</li>
    <li>AIRCRAFT SALES</li>
    <li>PILOT SERVICES</li>
    <li>CHARTER</li>
    <li>FLIGHT TRAINING</li>
  </ul>
  <div class="member">
    <span class="member-dot"></span>
    <span class="member-text"><span class="member-label">member of</span><span class="member-name">TFPS</span></span>
  </div>
</section>

</body>
</html>
```